Business Card Design Project

Hello! We need a business card design for a new company opening up in Downtown Dallas called Marbury Cupcakes. We are a cupcake factory and our primary colors are Tiffany Blue and Brown. We want to have a design that can be used for multiple positions (Owner/Operations Manager, Assistant Operations Manager, Decorator, Baker, Corporate Sale Rep, Special Events Rep etc) We would like for it to be double sided. Use the following information in your designs:

Renata Vankirk
Assistant Operations Manager
renata@marburycupcakes.example
T555.318.4907

Store Hours:
Mon-Thur 10am-9pm
Fri-Sat 10am-10pm
Sun 12pm-7pm

website: www.marburycupcakes.example

Address: 2735 Birch Ave, Dallas TX 70519

The logo is attached.

Industry/Entity Type

Business

Requirements
Must have
• It must be Tiffany Blue and Brown.
Nice to have
• Nice for it to be double sided.
Should not have
• No graphics like a cupcake. Just the word logo.

```html
<!DOCTYPE html>
<html lang="en">
<head>
<meta charset="utf-8">
<title>Marbury Cupcakes – Business Card</title>
<link href="https://fonts.googleapis.com/css2?family=Mulish:wght@400;500&display=swap" rel="stylesheet">
<style>
  :root {
    --backdrop: #e9e9e9;
    --card-white: #fbfbfb;
    --stripe-white: #f1f1f1;
    --tiffany: #6cbcc6;
    --tiffany-stripe: #79c4cd;
    --tiffany-panel: #6ab8c2;
    --tiffany-faint: #79c2cb;
    --brown: #5a2e22;
    --shadow: rgba(0, 0, 0, 0.18);
  }
  * { box-sizing: border-box; margin: 0; padding: 0; }
  html, body {
    width: 1200px; height: 900px; overflow: hidden;
    background: var(--backdrop);
    font-family: "Mulish", sans-serif;
    color: var(--brown);
  }
  .stage {
    width: 1200px; height: 900px;
    display: flex; flex-direction: column; align-items: center; justify-content: center;
    gap: 50px;
  }
  .card {
    width: 630px; height: 360px;
    position: relative;
    box-shadow: 0 6px 18px var(--shadow);
  }

  /* Front */
  .card-front {
    background: repeating-linear-gradient(90deg, var(--card-white) 0 22px, var(--stripe-white) 22px 44px);
  }
  .front-brand {
    position: absolute; left: 0; right: 0; top: 88px;
    text-align: center;
    font-size: 52px; font-weight: 400; letter-spacing: 0.5px;
    color: var(--tiffany);
  }
  .rule {
    position: absolute; left: 40px; right: 40px; height: 1.5px;
    background: var(--brown);
  }
  .rule-top { top: 190px; }
  .rule-bottom { top: 300px; }
  .hours {
    position: absolute; left: 0; right: 0; top: 218px;
    text-align: center; font-size: 17px; line-height: 1.55;
  }
  .hours-title { text-transform: uppercase; letter-spacing: 0.5px; }

  /* Back */
  .card-back {
    background: repeating-linear-gradient(90deg, var(--tiffany) 0 18px, var(--tiffany-stripe) 18px 36px);
  }
  .back-panel {
    position: absolute; inset: 16px;
    background: var(--tiffany-panel);
    border: 1.5px solid var(--brown);
    border-radius: 14px;
  }
  .back-brand {
    position: absolute; left: 0; right: 0; top: 22px;
    text-align: center; font-size: 54px; font-weight: 400;
    color: var(--tiffany-faint);
  }
  .person {
    position: absolute; left: 0; right: 0; top: 140px; text-align: center;
  }
  .person-name { font-size: 26px; font-weight: 500; }
  .person-title { font-size: 16px; margin-top: 2px; letter-spacing: 0.3px; }
  .back-rule {
    position: absolute; left: 110px; right: 36px; top: 220px; height: 1.5px;
    background: var(--brown);
  }
  .contact {
    position: absolute; left: 0; right: 0; top: 232px;
    text-align: center; font-size: 17px; line-height: 1.5;
  }
</style>
</head>
<body>
<main class="stage">
  <section class="card card-front" aria-label="Card front">
    <div class="front-brand">Marbury Cupcakes</div>
    <div class="rule rule-top"></div>
    <div class="hours">
      <div class="hours-title">Store Hours:</div>
      <div>Mon-Thur&nbsp; 10am-9pm | Fri-Sat&nbsp; 10am-10pm | Sun&nbsp; 12pm-7pm</div>
    </div>
    <div class="rule rule-bottom"></div>
  </section>

  <section class="card card-back" aria-label="Card back">
    <div class="back-panel">
      <div class="back-brand" aria-hidden="true">Marbury Cupcakes</div>
      <div class="person">
        <div class="person-name">Renata Vankirk</div>
        <div class="person-title">Assistant Operations Manager</div>
      </div>
      <div class="back-rule"></div>
      <div class="contact">
        <div>t: 555.318.4907 | e: renata@marburycupcakes.example</div>
        <div>2735 Birch Ave, Dallas TX 70519</div>
        <div>www.marburycupcakes.example</div>
      </div>
    </div>
  </section>
</main>
</body>
</html>
```